"The Craft of Patron Care," fourth edition cover design

Later this year, my publisher, Harold Penmarsh & Daughters, will issue a fourth, substantially revised edition of "The Craft of Patron Care," following the 2016 publication of the third edition and the second and first versions that were issued earlier.

To distinguish this new edition from previous ones, I need a cover design that visually connects and is consistent with what has preceded it, while signaling this is a new and different, worthy of prospective readers/buyers’ attention.

Attached are three different verbal approaches to the new cover; these are NOT MEANT to serve as actual designs, but rather will give you a sense of how language is to be deployed:

The first emphasizes “ART” as the key visual word in the book title;
The second emphasizes “CLIENT SERVICE” as the key visual words in the book title; and,
The third emphasizes just the word "CLIENT" in the book title.

A top-of-the-page is a pre-head that applies to all three versions:
“6 TIMELESS PRINCIPLES FOR ADVERTISING & MARKETING PRO’s
IN AN AI WORLD"

There's a mid-page sub-head for all three versions:
“THE CLASSIC GUIDE,” followed by
“FOURTH EDITION BY GERALD ASHCOMBE

And there's a one-line, bottom-of-the-page designation:
“Foreword by Mae Dunford, Global Executive Creative Director, Starbolt"

The pallette for the previously published third edition was black with red as an accent color on a field of white; I've attached a sample for reference, so you can see how it was executed. For this new fourth edition, I'd like to change the accent color from red to either Wedgewood blue, or British racing green, or an alternative that is assertive and color saturated -- think of primary colors -- that contrast sufficiently with the base of black. As an alternative, you can consider a cover that used either Wedgewood blue, British racing green, or another possibility as a full-bleed field, with copy content either revered out or surprinted.

Lastly, while the new cover largely is meant to be typographically driven, if you can come up with a visual metaphor that illustrates and builds on the book's title, that would be very helpful. By way of reference, the third edition's book cover attempted to do this by introducing a visual element at the end of the book's title that's meant to represent an artist's paint splatter (although I admit it didn't work as well as it should).

Target Market(s)

Prospective purchasers of the book who might discover copies at a bookstore, but more likely will encounter it through online distributors such as Riverdex, Hartwell & Pike, and Tindall’s.

Industry/Entity Type

Advertising and marketing

Font styles to use
Serif
Sans Serif
Other font styles liked:
• A mix of serif and san-serif typefaces is okay. for the examples I shared, I relieid on "Arial Rounded Bold" but you need not be weeded to this. If you opt to mix in a serif font, I am partial to Cambria as a typeface.

Requirements
Must have
• To achieve the goal of being “connected with but distinct” from previous editions, the new cover should be:  Largely typographic, but displaying a color palette different from the previous editions’ black-plus-red-accent on a canvas of white.  Any new accent color selected for use should be vibrant, strong, and highly saturated; think “British racing green,” “Wedgewood blue,” or their equivalents.  In addition to a powerful, “billboard” approach to type and color, consider other visual metaphors that are likely to engage the readers. The winning cover design will stand out from other books, while connecting with the previously published third edition.
Nice to have
• If you can find way to illustrate the book's title through a visual metaphor, that would be ideal.a
Should not have
• Anything that is frivolous or non-sensical

```html
<!DOCTYPE html>
<html lang="en">
<head>
<meta charset="utf-8">
<title>The Craft of Patron Care — Fourth Edition Cover</title>
<link rel="stylesheet" href="https://fonts.googleapis.com/css2?family=Montserrat:wght@400;500;700;800;900&display=swap">
<style>
  :root {
    --backdrop: #dedede;
    --cover-light: #f4f4f4;
    --cover-dark: #e6e6e6;
    --ink: #444444;
    --ink-deep: #333333;
    --accent: #55698f;
    --accent-soft: #6f86a7;
    --accent-light: #7b93b0;
  }
  * { margin: 0; padding: 0; box-sizing: border-box; }
  html, body {
    width: 1200px;
    height: 800px;
    overflow: hidden;
    background: var(--backdrop);
    font-family: "Montserrat", Arial, sans-serif;
  }
  .cover {
    position: absolute;
    left: 336px;
    top: 30px;
    width: 528px;
    height: 740px;
    background: linear-gradient(225deg, var(--cover-light) 0%, var(--cover-dark) 100%);
    color: var(--ink);
    text-align: center;
    box-shadow: 0 6px 18px rgba(0, 0, 0, 0.12);
  }
  .prehead {
    position: absolute;
    top: 52px;
    left: 0;
    right: 0;
    font-size: 13.5px;
    line-height: 17px;
    font-weight: 700;
    text-transform: uppercase;
    letter-spacing: 0.01em;
  }
  .prehead .accent { color: var(--accent-soft); font-weight: 800; }
  .title-the {
    position: absolute;
    top: 172px;
    left: 0;
    right: 0;
    font-size: 41px;
    font-weight: 900;
    line-height: 1;
    color: var(--ink);
  }
  .title-craft {
    position: absolute;
    top: 233px;
    left: 52px;
    width: 434px;
    height: 178px;
    display: block;
  }
  .title-rest {
    position: absolute;
    top: 428px;
    left: 52px;
    width: 434px;
    height: 46px;
    display: block;
  }
  .edition {
    position: absolute;
    top: 548px;
    left: 0;
    right: 0;
    font-size: 13.5px;
    line-height: 17px;
    font-weight: 700;
    text-transform: uppercase;
  }
  .edition .accent { color: var(--accent); font-weight: 800; }
  .credits {
    position: absolute;
    top: 645px;
    left: 0;
    right: 0;
    font-size: 10.5px;
    line-height: 13px;
    font-weight: 500;
    color: var(--ink-deep);
  }
</style>
</head>
<body>
  <main class="cover">
    <p class="prehead">
      <span class="accent">6 Timeless Principles</span><br>
      For Advertising &amp; Marketing Pro’s<br>
      <span class="accent">In an AI World</span>
    </p>

    <h1>
      <span class="title-the">THE</span>
      <svg class="title-craft" viewBox="0 0 660 128" preserveAspectRatio="none" aria-label="CRAFT">
        <defs>
          <linearGradient id="craftFill" x1="0" y1="1" x2="1" y2="0">
            <stop offset="0" stop-color="#52668d"/>
            <stop offset="1" stop-color="#7b93b0"/>
          </linearGradient>
        </defs>
        <text x="0" y="127" font-family="Montserrat, Arial, sans-serif" font-weight="900" font-size="180" textLength="660" lengthAdjust="spacingAndGlyphs" fill="url(#craftFill)">CRAFT</text>
      </svg>
      <svg class="title-rest" viewBox="0 0 434 46" aria-label="OF PATRON CARE">
        <text x="0" y="41" font-family="Montserrat, Arial, sans-serif" font-weight="800" font-size="44" textLength="434" lengthAdjust="spacingAndGlyphs"><tspan fill="#333333">OF </tspan><tspan fill="#55698f">PATRON</tspan><tspan fill="#444444"> CARE</tspan></text>
      </svg>
    </h1>

    <p class="edition">
      The Classic Guide<br>
      <span class="accent">Fourth Edition</span>
    </p>

    <p class="credits">
      by GERALD ASHCOMBE<br>
      Foreword by Mae Dunford, Global Executive Creative Director, Starbolt
    </p>
  </main>
</body>
</html>
```